Dental Business Card

We are looking for a double sided business card that can be easily customized with the names of the different members of our dental team.

I would like the background to be the 2-tone blue fleur-de-lis type pattern on the sides of our website (www.harborvalebrights.com).

I would like the logo attached incorporated.

I would like our address (2847 Birchmont Court, Suite 240, Harborvale, OR 97381), phone number (555-318-4902), fax number (555-318-4977), website (www.harborvalebrights.com), and email address (info@harborvalebrights.com) all included on the front side.

Something a little more artistic to complement/highlight the logo on the back would be interesting.

I would like the business card to look professional, slightly feminine, and expense.

```html
<!DOCTYPE html>
<html lang="en">
<head>
<meta charset="utf-8">
<title>Harborvale Brights – Business Card</title>
<link rel="stylesheet" href="https://fonts.googleapis.com/css2?family=Cinzel:wght@400;700&family=Cormorant+Garamond:wght@500&family=Great+Vibes&display=swap">
<style>
  :root {
    --bg-light: #bcd5e8;
    --bg-mid: #a9c8e0;
    --ink-deep: #1c3f8c;
    --ink-royal: #1f5fb8;
    --ink-bright: #2f86dc;
    --rule: #3b8ad6;
  }
  * { margin: 0; padding: 0; box-sizing: border-box; }
  html, body { width: 1200px; height: 678px; overflow: hidden; }
  body { background: var(--bg-light); }

  .card {
    position: relative;
    width: 1200px;
    height: 678px;
    overflow: hidden;
  }
  .damask-field {
    position: absolute;
    inset: 0;
    background: radial-gradient(ellipse at 50% 45%, var(--bg-light) 0%, var(--bg-mid) 100%);
  }

  .brand-mark {
    position: absolute;
    left: 40px;
    top: 100px;
    width: 320px;
    display: flex;
    align-items: center;
    gap: 18px;
  }
  .brand-mark__dot {
    width: 70px;
    height: 70px;
    border-radius: 50%;
    background: var(--ink-royal);
    flex: none;
  }
  .brand-mark__name {
    font-family: "Cinzel", serif;
    font-weight: 700;
    font-size: 36px;
    line-height: 1.15;
    color: var(--ink-royal);
  }

  .dentist-name {
    position: absolute;
    left: 440px;
    top: 98px;
    width: 700px;
    text-align: center;
    font-family: "Cinzel", serif;
    font-weight: 700;
    font-size: 52px;
    letter-spacing: 1px;
    color: var(--ink-royal);
    text-shadow: 3px 4px 5px rgba(20, 40, 80, 0.45);
    white-space: nowrap;
  }
  .slogan {
    position: absolute;
    left: 440px;
    top: 170px;
    width: 700px;
    text-align: center;
    font-family: "Great Vibes", cursive;
    font-size: 60px;
    line-height: 1.1;
    color: var(--ink-royal);
    text-shadow: 2px 3px 4px rgba(20, 40, 80, 0.35);
    white-space: nowrap;
  }

  .practice {
    position: absolute;
    left: 0;
    top: 416px;
    width: 100%;
    text-align: center;
  }
  .practice__name {
    font-family: "Cinzel", serif;
    font-weight: 400;
    font-size: 46px;
    color: var(--ink-deep);
    line-height: 1;
  }
  .practice__name .accent { color: var(--ink-bright); }
  .practice__rule {
    margin: 10px 16px 0;
    display: flex;
    align-items: center;
    gap: 14px;
  }
  .practice__rule::before,
  .practice__rule::after {
    content: "";
    flex: 1;
    height: 2px;
    background: var(--rule);
  }
  .practice__tagline {
    font-family: "Cormorant Garamond", serif;
    font-weight: 500;
    font-size: 21px;
    letter-spacing: 1px;
    color: var(--ink-deep);
    text-transform: uppercase;
  }

  .contact {
    position: absolute;
    top: 528px;
    font-family: "Cinzel", serif;
    font-weight: 700;
    font-size: 22px;
    letter-spacing: 1.5px;
    line-height: 32px;
    color: var(--ink-deep);
    font-style: normal;
  }
  .contact--online { left: 40px; }
  .contact--address { right: 49px; text-align: right; }
</style>
</head>
<body>
  <main class="card">
    <div class="damask-field" role="img" aria-label="Two-tone blue damask fleur-de-lis background pattern"></div>

    <div class="brand-mark">
      <span class="brand-mark__dot"></span>
      <span class="brand-mark__name">Harborvale<br>Brights</span>
    </div>

    <h1 class="dentist-name">Dr. Elena R. Whitfield</h1>
    <p class="slogan">We make beautiful smiles!</p>

    <section class="practice">
      <h2 class="practice__name">Harborvale <span class="accent">Brights</span></h2>
      <div class="practice__rule"><span class="practice__tagline">The Art of Dentistry</span></div>
    </section>

    <address class="contact contact--online">
      www.harborvalebrights.com<br>
      info@harborvalebrights.com<br>
      Ph. 555-318-4902<br>
      Fax. 555-318-4977
    </address>

    <address class="contact contact--address">
      2847 Birchmont Court, Suite 240,<br>
      Harborvale, OR 97381
    </address>
  </main>
</body>
</html>
```